Business card design needed to incorporate existing logo

We need a business card for a new modern Accounting & Business Solutions company call Kelvra Partners.com.au servicing all of Australia.
My tagline is Steady Ledger Answers... done right.

We specialise in Cloud Accounting and this is our primary focus. We also provide tax representation, debt recovery, computer, tablet and smart phone sales.

I would like a design that uses my corporate, trustworthy colours of blue/white, black/grey however am open to suggestion. I have attached my logo to go on the card somewhere,of which you will see the colour scheme.

I am after a card that STANDS OUT, somewhere between it not being too busy and not being a baron waste of space.

A 'cloud' incorporated in the design may work well, up to your artistic judgement. I know what I like when I see it; it is harder to put into words!

Excited to see your ideas!
I have added my logo predominately (blue/white) and for additional opportunity have added my reverse logo (darker one). I have used the blue/white on my website and letterhead. I will be using both on my vehicle signage.

Target Market(s)

Tradesmen and small-medium businesses of all descriptions Australia-wide

Industry/Entity Type

Debt

Contact Information for Business Card

Dale Fenwick
Principal (optional)
Kelvra Partners.com.au
Steady Ledger Answers... done right

P: 1800 530 918
M: 0418 652 074 (optional)
W: www.kelvrapartners.example
E: admin@kelvrapartners.example

Logo Text

Steady Ledger Answers... done right!

Logo styles of interest
Wordmark Logo
Requirements
Must have
• Must look professional and of high quality not cheap.

My logo and my tagline 'Steady Ledger Answers... done right'.

I have my colourscheme in mind as per my attached logo, however am open to suggestion. I want to see what you can create that I would not have thought of.

Modern, innovative.
Something I won't look at and think, 'I could have done that myself'.

Must be able to be printed on Plimo 300gm premium cards and the artwork provided to me.
Nice to have
• Title of Principal is optional depending on space and judement call of look/fee.
M: (mobile) number is also optional as above.

Somthing cloud related given the Cloud Accounting aspect may be relevant. I leave it to your artistic design and judgement.
Should not have
• Must not look cheap.

```html
<!DOCTYPE html>
<html lang="en">
<head>
<meta charset="utf-8">
<title>Kelvra Partners – Business Card</title>
<link rel="stylesheet" href="https://fonts.googleapis.com/css2?family=Jost:wght@300&family=Mulish:wght@600;700;800&display=swap">
<style>
  :root {
    --stage: #4b2d1f;
    --front-blue: #215e8e;
    --front-blue-light: #2f6f9f;
    --back-navy: #191a52;
    --back-navy-light: #262f6c;
    --row-fill: #2b3c77;
    --accent-bar: #2a5e93;
    --white: #ffffff;
    --soft-white: #e9ecf5;
  }
  * { box-sizing: border-box; margin: 0; padding: 0; }
  html, body {
    width: 1200px; height: 1181px; overflow: hidden;
    background: var(--stage);
  }
  .canvas { position: relative; width: 1200px; height: 1181px; }

  .card {
    position: absolute; left: 256px; width: 687px; height: 395px;
    box-shadow: 0 6px 18px rgba(0,0,0,0.45);
    overflow: hidden;
  }

  /* Front */
  .card-front {
    top: 166px;
    background: radial-gradient(ellipse 60% 70% at 50% 28%, var(--front-blue-light), var(--front-blue) 75%);
  }
  .wordmark {
    position: absolute; left: 0; right: 0; top: 308px;
    text-align: center; color: var(--white);
    font-family: "Jost", sans-serif; font-weight: 300;
  }
  .card-front .wordmark { top: 142px; }
  .wordmark-name {
    display: block; font-size: 78px; line-height: 1; letter-spacing: 6px;
  }
  .wordmark-domain {
    display: block; margin-top: 6px; font-size: 27px; letter-spacing: 5px;
  }

  /* Back */
  .card-back {
    top: 612px;
    background: radial-gradient(ellipse 55% 60% at 50% 38%, var(--back-navy-light), var(--back-navy) 80%);
    font-family: "Mulish", sans-serif; color: var(--white);
  }
  .accent-bar {
    position: absolute; left: 227px; width: 233px; height: 10px;
    background: var(--accent-bar);
  }
  .accent-bar.top { top: 0; }
  .accent-bar.bottom { bottom: 0; }

  .tagline {
    position: absolute; top: 26px; left: 0; right: 0; text-align: center;
    font-size: 13px; font-weight: 700;
  }
  .holder {
    position: absolute; top: 133px; left: 0; right: 0; text-align: center;
  }
  .holder-name { font-size: 30px; font-weight: 800; letter-spacing: -0.3px; line-height: 1.05; }
  .holder-title {
    font-size: 14px; font-weight: 800; letter-spacing: 15px; margin-left: 15px;
  }

  .contact-row {
    position: absolute; left: 59px; width: 569px; height: 41px;
    display: flex; gap: 4px;
  }
  .contact-row.phones { top: 266px; }
  .contact-row.online { top: 311px; }
  .icon-box {
    width: 35px; height: 41px; background: var(--row-fill);
    display: flex; align-items: center; justify-content: center;
  }
  .icon-box svg { width: 18px; height: 18px; }
  .info-box {
    flex: 1; background: var(--row-fill);
    display: flex; justify-content: space-between; align-items: center;
    padding: 0 11px 0 12px; font-size: 13px; font-weight: 700;
    color: var(--soft-white);
  }
  .phones .info-box { letter-spacing: 3.2px; }
  .online .info-box { letter-spacing: 0.2px; }
</style>
</head>
<body>
<div class="canvas">

  <section class="card card-front">
    <div class="wordmark">
      <span class="wordmark-name">KELVRA</span>
      <span class="wordmark-domain">PARTNERS.COM.AU</span>
    </div>
  </section>

  <section class="card card-back">
    <div class="accent-bar top"></div>
    <p class="tagline">Steady Ledger Answers... done right</p>

    <div class="holder">
      <p class="holder-name">Dale Fenwick</p>
      <p class="holder-title">Principal</p>
    </div>

    <div class="contact-row phones">
      <div class="icon-box">
        <svg viewBox="0 0 18 18" aria-label="Mobile">
          <rect x="5" y="2" width="8" height="14" rx="1.2" fill="none" stroke="#e9ecf5" stroke-width="1.3"/>
          <rect x="7" y="5" width="4" height="4" fill="none" stroke="#e9ecf5" stroke-width="1"/>
        </svg>
      </div>
      <div class="info-box"><span>0418 652 074</span><span>1800 530 918</span></div>
      <div class="icon-box">
        <svg viewBox="0 0 18 18" aria-label="Telephone">
          <path d="M2 7 Q9 2 16 7 L14.5 9 L12 8 L12 6.5 Q9 5.5 6 6.5 L6 8 L3.5 9 Z" fill="none" stroke="#e9ecf5" stroke-width="1.1"/>
          <path d="M4 10 L14 10 L15 15 L3 15 Z" fill="none" stroke="#e9ecf5" stroke-width="1.1"/>
          <circle cx="9" cy="12.5" r="1.4" fill="none" stroke="#e9ecf5" stroke-width="1"/>
        </svg>
      </div>
    </div>

    <div class="contact-row online">
      <div class="icon-box">
        <svg viewBox="0 0 18 18" aria-label="Website">
          <circle cx="9" cy="9" r="7" fill="none" stroke="#e9ecf5" stroke-width="1.2"/>
          <ellipse cx="9" cy="9" rx="3" ry="7" fill="none" stroke="#e9ecf5" stroke-width="1"/>
          <line x1="2" y1="9" x2="16" y2="9" stroke="#e9ecf5" stroke-width="1"/>
          <line x1="3" y1="5.5" x2="15" y2="5.5" stroke="#e9ecf5" stroke-width="0.9"/>
          <line x1="3" y1="12.5" x2="15" y2="12.5" stroke="#e9ecf5" stroke-width="0.9"/>
        </svg>
      </div>
      <div class="info-box"><span>www.kelvrapartners.example</span><span>admin@kelvrapartners.example</span></div>
      <div class="icon-box">
        <svg viewBox="0 0 18 18" aria-label="Email">
          <circle cx="9" cy="9" r="2.8" fill="none" stroke="#e9ecf5" stroke-width="1.3"/>
          <path d="M11.8 6.5 L11.8 10.5 Q11.8 12.5 13.6 12.5 Q16 12.5 16 9 A7 7 0 1 0 12.5 15" fill="none" stroke="#e9ecf5" stroke-width="1.3"/>
        </svg>
      </div>
    </div>

    <div class="accent-bar bottom"></div>
  </section>

</div>
</body>
</html>
```